Place holder for book called THE AUDACITY OF DAWN

I'm relying on your imaginative genius because I have no suggestions for you. Attached is a picture of the author when young if it will be of help. The only other info I can offer is that the author uses the alphabet as a theme.

Book info:
Title: THE AUDACITY OF DAWN
Author: ROSALIND MCARDLE

This is a memoir. It's a story of daring to hope when things seem hopeless, of problems when changing countries, of making success of dross. I'm looking for a design that is daring, eye-catching but promises hope. I hope it's not impossible.

Can you give me a place holder for the book to go onto my website and for pre-publicity? Then, in 6-9 months I'll pay another $150 for the completion of hardcover, paperback and ebook covers.

```html
<!DOCTYPE html>
<html lang="en">
<head>
<meta charset="utf-8">
<title>The Audacity of Dawn — Rosalind McArdle</title>
<link rel="stylesheet" href="https://fonts.googleapis.com/css2?family=Great+Vibes&family=Josefin+Sans:wght@600&display=swap">
<style>
  :root {
    --backdrop: #d9d6d3;
    --paper: #fbfbfb;
    --ink: #0c0c0c;
    --ink-soft: #3a3a3a;
    --reverse: #ffffff;
  }
  * { box-sizing: border-box; margin: 0; padding: 0; }
  html, body {
    width: 1200px;
    height: 1200px;
    overflow: hidden;
    background: var(--backdrop);
  }
  .canvas {
    position: relative;
    width: 1200px;
    height: 1200px;
    display: flex;
    align-items: center;
    justify-content: center;
  }
  .cover {
    position: relative;
    width: 700px;
    height: 1140px;
    background: var(--paper);
    overflow: hidden;
    box-shadow: 0 10px 30px rgba(0,0,0,0.18);
  }
  .cover__art,
  .cover__band {
    position: absolute;
    left: 0;
    top: 0;
    width: 700px;
    height: 1140px;
  }
  .art-stop-ink { stop-color: var(--ink); }
  .cover__band path { fill: var(--ink); }
  .cover__title {
    position: absolute;
    left: 0;
    top: 765px;
    width: 700px;
    text-align: center;
    font-family: "Great Vibes", cursive;
    font-weight: 400;
    color: var(--reverse);
    font-size: 112px;
    line-height: 0.85;
    word-spacing: 0.18em;
    white-space: nowrap;
  }
  .cover__title span { display: block; }
  .cover__title .title-second { padding-left: 60px; }
  .cover__author {
    position: absolute;
    left: 0;
    bottom: 18px;
    width: 700px;
    text-align: center;
    font-family: "Josefin Sans", sans-serif;
    font-weight: 600;
    font-size: 30px;
    letter-spacing: 0.2em;
    color: var(--ink);
    white-space: nowrap;
  }
</style>
</head>
<body>
  <main class="canvas">
    <article class="cover">
      <svg class="cover__art" viewBox="0 0 700 1140" role="img" aria-label="Illustration of a bird in flight dissolving into scattered alphabet letters">
        <defs>
          <radialGradient id="fade-strong">
            <stop offset="0" class="art-stop-ink" stop-opacity="1"/>
            <stop offset="0.55" class="art-stop-ink" stop-opacity="0.85"/>
            <stop offset="1" class="art-stop-ink" stop-opacity="0"/>
          </radialGradient>
          <radialGradient id="fade-mid">
            <stop offset="0" class="art-stop-ink" stop-opacity="0.85"/>
            <stop offset="0.6" class="art-stop-ink" stop-opacity="0.4"/>
            <stop offset="1" class="art-stop-ink" stop-opacity="0"/>
          </radialGradient>
          <radialGradient id="fade-soft">
            <stop offset="0" class="art-stop-ink" stop-opacity="0.35"/>
            <stop offset="1" class="art-stop-ink" stop-opacity="0"/>
          </radialGradient>
        </defs>
        <ellipse cx="460" cy="240" rx="230" ry="70" transform="rotate(22 460 240)" fill="url(#fade-strong)"/>
        <ellipse cx="330" cy="420" rx="170" ry="120" transform="rotate(-25 330 420)" fill="url(#fade-mid)"/>
        <ellipse cx="170" cy="600" rx="160" ry="80" transform="rotate(-30 170 600)" fill="url(#fade-soft)"/>
      </svg>
      <svg class="cover__band" viewBox="0 0 700 1140" aria-hidden="true">
        <path d="M0,830 Q350,570 700,820 L700,1065 Q400,1040 0,1105 Z"/>
      </svg>
      <h1 class="cover__title">
        <span class="title-first">The Audacity</span>
        <span class="title-second">of Dawn</span>
      </h1>
      <p class="cover__author">ROSALIND MCARDLE</p>
    </article>
  </main>
</body>
</html>
```